Business card for law firm

Need business card for new law firm. Think confident, authoritative, conservative, but not stuffy or old-fashioned.

Contact Information for Business Card

Content for card - logo (uploaded), plus the following:

Paul Wexbury (larger font)
Managing Partner (larger font, but not as large as name)
Level 9, 41 Tansy Lane
Sydney NSW 2000
Main Tel 02 7346 2190
Direct Tel 02 6273 4415
Email paul@qvlegal.com.au
www.qvlegal.com.au

Letterhead design should include logo plus:
Level 9, 41 Tansy Lane
Sydney NSW 2000
Tel 02 6273 4415
www.qvlegal.com.au

```html
<!DOCTYPE html>
<html lang="en">
<head>
<meta charset="utf-8">
<title>Quayvale Legal – Business Card</title>
<link rel="stylesheet" href="https://fonts.googleapis.com/css2?family=Dancing+Script:wght@700&family=Roboto:wght@400&display=swap">
<style>
  :root {
    --backdrop: #d0d1d3;
    --card: #ffffff;
    --navy: #1f2459;
    --ink: #111111;
    --gavel-dark: #1f2459;
    --gavel-light: #4a4f80;
  }
  html, body {
    margin: 0;
    width: 1200px;
    height: 1200px;
    overflow: hidden;
    background: var(--backdrop);
  }
  .card {
    position: absolute;
    left: 216px;
    top: 380px;
    width: 768px;
    height: 439px;
    background: var(--card);
    font-family: "Roboto", Arial, sans-serif;
    color: var(--ink);
  }
  .brand {
    position: absolute;
    left: 40px;
    top: 30px;
    width: 332px;
    text-align: center;
  }
  .brand-square {
    display: block;
    width: 64px;
    height: 64px;
    margin: 10px auto 40px;
    background: var(--navy);
  }
  .brand-name {
    margin: 0;
    font-size: 29px;
    font-weight: 400;
    letter-spacing: 3px;
    color: var(--navy);
    line-height: 1.2;
  }
  .gavel-art {
    position: absolute;
    left: 120px;
    top: 251px;
    width: 174px;
    height: 140px;
    border-radius: 10px;
    background: linear-gradient(135deg, var(--gavel-light), var(--gavel-dark));
  }
  .person {
    position: absolute;
    left: 420px;
    top: 18px;
  }
  .person-name {
    margin: 0;
    font-family: "Dancing Script", cursive;
    font-weight: 700;
    font-size: 48px;
    line-height: 1.1;
    color: var(--ink);
  }
  .person-title {
    margin: 4px 0 0;
    font-size: 26px;
    color: var(--navy);
    line-height: 1.2;
  }
  .contacts {
    position: absolute;
    left: 420px;
    top: 213px;
    margin: 0;
    padding: 0;
    list-style: none;
    font-size: 20px;
    line-height: 27px;
  }
  .contact {
    display: flex;
    align-items: flex-start;
    margin-bottom: 9px;
  }
  .contact-icon {
    width: 30px;
    height: 30px;
    margin-right: 14px;
    flex: none;
    fill: var(--navy);
  }
  .contact-text { margin: 0; }
  .contact--email, .contact--web { align-items: center; }
  .contact--web { margin-top: 14px; }
</style>
</head>
<body>
  <main class="card">
    <div class="brand">
      <span class="brand-square"></span>
      <p class="brand-name">QUAYVALE LEGAL</p>
    </div>

    <div class="gavel-art" role="img" aria-label="Illustration of a judge's gavel resting on its sound block"></div>

    <header class="person">
      <h1 class="person-name">Paul Wexbury</h1>
      <p class="person-title">Managing Partner</p>
    </header>

    <ul class="contacts">
      <li class="contact contact--address">
        <svg class="contact-icon" viewBox="0 0 30 30" aria-hidden="true">
          <path d="M15 1c-6 0-10 4.4-10 10 0 7 10 18 10 18s10-11 10-18c0-5.6-4-10-10-10zm0 14a4.2 4.2 0 1 1 0-8.4 4.2 4.2 0 0 1 0 8.4z"/>
        </svg>
        <p class="contact-text">Level 9, 41 Tansy Lane<br>Sydney NSW 2000</p>
      </li>
      <li class="contact contact--phone">
        <svg class="contact-icon" viewBox="0 0 30 30" aria-hidden="true">
          <rect x="12" y="0" width="2.5" height="5" rx="1"/>
          <path d="M10 4h10a3 3 0 0 1 3 3v19a3 3 0 0 1-3 3H10a3 3 0 0 1-3-3V7a3 3 0 0 1 3-3zm0 4v7h10V8zm5 13a1.8 1.8 0 1 0 0 3.6 1.8 1.8 0 0 0 0-3.6z" fill-rule="evenodd"/>
        </svg>
        <p class="contact-text">02 7346 2190<br>02 6273 4415</p>
      </li>
      <li class="contact contact--email">
        <svg class="contact-icon" viewBox="0 0 30 30" aria-hidden="true">
          <path d="M1 6h28v18H1zm3 2.5 11 8.5 11-8.5zM3 9.5v12.3l7.3-6.7zm24 0-7.3 5.6 7.3 6.7zM12 16.4 4.4 22h21.2L18 16.4l-3 2.3z" fill-rule="evenodd"/>
        </svg>
        <p class="contact-text">paul@qvlegal.com.au</p>
      </li>
      <li class="contact contact--web">
        <svg class="contact-icon" viewBox="0 0 30 30" aria-hidden="true">
          <path d="M14 1a13 13 0 1 0 2 25.8l-.6-2.3A10.6 10.6 0 0 1 14 24.6c-1.5-1.4-2.6-4-2.9-7.1h5.4l-.5-2.4h-5c.1-3.3 1.3-6.3 3-8.1V1zm-2.6 2.6C10 5.5 9 8.1 8.8 11H4.5a10.7 10.7 0 0 1 6.9-7.4zM16.6 3.6A10.7 10.7 0 0 1 23.5 11h-4.3c-.2-2.9-1.2-5.5-2.6-7.4zM4 13.4h4.7v1.7H4zm0 4h4.8c.3 2.8 1.2 5.3 2.6 7.1A10.7 10.7 0 0 1 4 17.4zM16 6v5h2v-5zm7 7.4h3v1.7h-3z"/>
          <path d="M17 14l11 5-4.6 1.4 3.6 5-2.2 1.6-3.6-5L18 26z"/>
        </svg>
        <p class="contact-text">www.qvlegal.com.au</p>
      </li>
    </ul>
  </main>
</body>
</html>
```